Business Card Design Project

Use our current logo. Clean design.

Industry/Entity Type

Business

Requirements
Must have
• Marisela DUCRANTE
M. Law
Managing Partner

Velotrana AG
Brunnmattweg 274
CH-3097 Liebefeld

M. +41 79 418 26 97
T. +41 31 742 19 04
F. +41 31 742 19 38

m.ducrante@velotrana.example
www.velotrana.example

```html
<!DOCTYPE html>
<html lang="en">
<head>
<meta charset="utf-8">
<title>Velotrana AG – Business Card</title>
<link rel="stylesheet" href="https://fonts.googleapis.com/css2?family=Noto+Sans:wght@400;700&display=swap">
<style>
  :root {
    --backdrop: #ecebe8;
    --card: #ffffff;
    --ink: #1c1c1c;
    --ink-soft: #2a2a2a;
    --rule: #9a9a9a;
    --icon: #a3a3a3;
    --swoosh: #b9b9b9;
    --shadow: rgba(0, 0, 0, 0.28);
  }
  * { box-sizing: border-box; margin: 0; padding: 0; }
  html, body {
    width: 1200px;
    height: 1000px;
    overflow: hidden;
    background: var(--backdrop);
    font-family: "Noto Sans", Verdana, sans-serif;
    color: var(--ink);
  }
  .canvas { position: relative; width: 1200px; height: 1000px; }

  .card {
    position: absolute;
    width: 728px;
    height: 416px;
    background: var(--card);
    box-shadow: 4px 6px 14px var(--shadow);
  }

  /* Back side */
  .card-back { left: 400px; top: 70px; }
  .card-back .band-rule {
    position: absolute;
    left: 0; right: 0;
    height: 1px;
    background: var(--rule);
  }
  .band-rule.upper { top: 119px; }
  .band-rule.lower { top: 297px; }
  .brand-name {
    position: absolute;
    left: 0; right: 0;
    top: 182px;
    text-align: center;
    font-size: 34px;
    font-weight: 400;
    letter-spacing: 3px;
    color: var(--ink);
  }

  /* Front side */
  .card-front { left: 168px; top: 471px; }
  .holder {
    position: absolute;
    left: 0; width: 728px;
    top: 70px;
    text-align: center;
    padding-left: 2px;
  }
  .holder-name {
    font-size: 23px;
    font-weight: 700;
    color: var(--ink);
    line-height: 32px;
  }
  .holder-title {
    font-size: 21px;
    font-weight: 400;
    color: var(--ink-soft);
    line-height: 30px;
  }
  .swoosh {
    position: absolute;
    left: 76px;
    top: 150px;
    width: 578px;
    height: 12px;
  }

  .contact-list {
    position: absolute;
    list-style: none;
  }
  .contact-list li {
    display: flex;
    align-items: center;
    height: 27px;
    font-size: 14px;
    letter-spacing: 0.4px;
    color: var(--ink);
  }
  .contact-list li.address { font-size: 12.5px; letter-spacing: 0.1px; }
  .contact-list svg {
    width: 20px;
    height: 18px;
    margin-right: 14px;
    flex: none;
    fill: var(--icon);
  }
  .contact-web { left: 72px; top: 253px; }
  .contact-phone { left: 500px; top: 254px; }
  .contact-phone svg { margin-right: 13px; }
</style>
</head>
<body>
<main class="canvas">

  <section class="card card-back" aria-label="Card back">
    <div class="band-rule upper"></div>
    <p class="brand-name">VELOTRANA</p>
    <div class="band-rule lower"></div>
  </section>

  <section class="card card-front" aria-label="Card front">
    <header class="holder">
      <p class="holder-name">Marisela DUCRANTE M. Law</p>
      <p class="holder-title">Managing Partner</p>
    </header>

    <svg class="swoosh" viewBox="0 0 578 12" preserveAspectRatio="none" aria-hidden="true">
      <path d="M0 3 Q290 1 578 2 Q420 4 290 10 Q150 4 0 3 Z" fill="var(--swoosh)"/>
    </svg>

    <ul class="contact-list contact-web">
      <li>
        <svg viewBox="0 0 20 18" aria-hidden="true"><rect x="1" y="1" width="18" height="16" rx="4"/><circle cx="10" cy="9" r="5" fill="none" stroke="#fff" stroke-width="1.2"/><path d="M5 9h10M10 4v10" stroke="#fff" stroke-width="1"/></svg>
        velotrana.example
      </li>
      <li>
        <svg viewBox="0 0 20 18" aria-hidden="true"><rect x="1" y="3" width="18" height="12" rx="1"/><path d="M1.5 3.5 10 10l8.5-6.5" fill="none" stroke="#fff" stroke-width="1.3"/></svg>
        m.ducrante@velotrana.example
      </li>
      <li class="address">
        <svg viewBox="0 0 20 18" aria-hidden="true"><path d="M10 1a5.5 5.5 0 0 0-5.5 5.5C4.5 11 10 17 10 17s5.5-6 5.5-10.5A5.5 5.5 0 0 0 10 1z"/><circle cx="10" cy="6.5" r="2" fill="#fff"/></svg>
        Velotrana AG Brunnmattweg 274 CH-3097 Liebefeld
      </li>
    </ul>

    <ul class="contact-list contact-phone">
      <li>
        <svg viewBox="0 0 20 18" aria-hidden="true"><rect x="5" y="0.5" width="10" height="17" rx="2"/><rect x="6.5" y="2.5" width="7" height="11" fill="#fff"/><circle cx="10" cy="15.5" r="0.9" fill="#fff"/></svg>
        +41 79 418 26 97
      </li>
      <li>
        <svg viewBox="0 0 20 18" aria-hidden="true"><path d="M5 1.5 7.6 1l1.6 4-1.8 1.4a9 9 0 0 0 4.4 4.6l1.5-1.7 4 1.6-.5 2.6c-.3 1.4-1.8 2.3-3.2 1.9C8.4 14.1 4 9.6 3.3 4.6 3.1 3.2 3.8 1.8 5 1.5z"/></svg>
        +41 31 742 19 04
      </li>
      <li>
        <svg viewBox="0 0 20 18" aria-hidden="true"><rect x="5" y="1" width="10" height="6" fill="none" stroke="var(--icon)" stroke-width="1.5"/><rect x="1" y="6" width="18" height="10" rx="2"/><rect x="5" y="10" width="10" height="1.5" fill="#fff"/><rect x="5" y="13" width="10" height="1.5" fill="#fff"/></svg>
        +41 31 742 19 38
      </li>
    </ul>
  </section>

</main>
</body>
</html>
```